Webdesign für Bäckerei
Zielgruppe
Bäckerei in der 4. Generation im Herzen des Erzgebirges
Aufgabenstellung
Vom Kunden gibt ees keine Vorgaben oder Wünsche. Die Kunden möchten sich überraschen lassen.
Die Webseite sollte dennoch modern, frisch und einladend wirken.
In den Farben Rot/Gelb (eventuell eher gold). Bitte Akzente dezent einsetzen.
Wir wünschen uns eine geschwungene, etwas ausgefallenere Schriftart.
Das Logo bitte in einer angemessenen Form verwenden.
Bitte keine Figma Datei.

```html
<!DOCTYPE html>
<html lang="de">
<head>
<meta charset="utf-8">
<title>Bäckerei Lindner – Startseite</title>
<link href="https://fonts.googleapis.com/css2?family=Alex+Brush&family=Jost:wght@400;500;600&family=Libre+Baskerville:wght@400;700&display=swap" rel="stylesheet">
<style>
:root{
  --cream:#fdf6dc;
  --cream-2:#fbf1cf;
  --gold:#e0a43a;
  --gold-dark:#d08a22;
  --script:#d4892a;
  --red:#c8282b;
  --ink:#3d3a36;
  --muted:#6b655d;
  --white:#ffffff;
}
*{box-sizing:border-box;margin:0;padding:0}
html,body{width:1200px;height:3487px;overflow:hidden;background:var(--white)}
body{position:relative;font-family:"Jost",sans-serif;color:var(--ink)}
.abs{position:absolute}
.script{font-family:"Alex Brush",cursive;color:var(--script);font-weight:400}

/* header */
.site-header{left:0;top:0;width:1200px;height:162px;background:var(--cream)}
.brand{left:480px;top:18px;width:240px;height:80px;display:flex;align-items:center;justify-content:center;gap:10px;font-size:30px;font-weight:600;color:var(--red)}
.brand .dot{width:14px;height:14px;border-radius:50%;background:var(--gold)}
.nav{left:122px;top:132px;display:flex;gap:18px;font-size:14px;font-weight:500;color:var(--ink)}
.search{left:72px;top:132px}
.user-icons{left:990px;top:128px;display:flex;gap:12px}
.user-icons span{width:26px;height:26px;border-radius:50%;background:#6e6a66}
.cart{left:1071px;top:124px;font-size:13px;line-height:17px;color:var(--muted)}
.cart b{display:block;font-weight:500;color:var(--gold-dark);font-family:"Libre Baskerville",serif;font-size:13px}

/* hero */
.hero{left:0;top:162px;width:1200px;height:420px;background:#f3efe8}
.hero-photo{left:520px;top:0;width:680px;height:420px;background:linear-gradient(90deg,#f3efe8 0%,#f0e6d6 30%,#e8cfa8 55%,#f4f0ea 75%,#e9e4dc 100%)}
.hero h1{left:130px;top:70px;font-size:46px;line-height:51px;color:var(--script)}
.hero p{left:131px;top:198px;font-size:16.5px;line-height:26.5px;font-weight:500;color:#4a4540}
.btn{background:var(--gold);color:var(--white);font-weight:600;letter-spacing:1px;display:flex;align-items:center;justify-content:center;border-radius:5px}
.hero .btn{left:131px;top:311px;width:209px;height:36px;font-size:16px}

/* features */
.features{left:0;top:582px;width:1200px;height:146px;background:var(--cream)}
.feature{top:44px;display:flex;align-items:center;gap:14px}
.feature .ico{width:72px;height:56px;border-radius:10px;background:linear-gradient(135deg,#f2c14e,#3d3a36)}
.feature h3{font-size:16.5px;font-weight:500;color:var(--ink)}
.feature p{font-size:12.5px;color:var(--muted)}

/* section titles */
.sec-title{font-size:30px;text-align:center;width:1200px;left:0}
.sec-title i{display:inline-block;width:6px;height:6px;border-radius:50%;background:var(--gold);vertical-align:middle;margin:0 22px}

/* news cards */
.news{top:827px;width:520px;height:253px;background:var(--cream);border-radius:12px;overflow:hidden}
.news .photo{left:0;top:0;width:270px;height:253px}
.news .off{left:0;bottom:0;width:100px;height:100px;background:#f6c51a;border-top-right-radius:100px;color:var(--white);font-size:28px;line-height:38px;padding:20px 0 0 16px}
.news h3{left:286px;top:16px;font-size:25px}
.news p{left:286px;top:59px;width:215px;font-size:16.5px;line-height:26.4px;color:#5c5650}
.dots{left:545px;top:1098px;display:flex;gap:17px}
.dots span{width:13px;height:13px;border-radius:50%;background:#f5efcc}
.dots span.on{background:var(--red)}

/* category grid */
.cat{width:341px;height:236px;border-radius:12px;overflow:hidden;background:var(--cream)}
.cat .photo{left:0;top:0;width:341px;height:236px}
.cat .label{left:0;bottom:0;width:341px;height:50px;background:rgba(253,246,220,.85);text-align:center;font-size:29px;line-height:50px}

/* mobile bakery */
.mobile{left:16px;top:1786px;width:1184px;height:187px;background:var(--cream)}
.mobile h2{left:88px;top:20px;font-size:42px}
.mobile .btn{left:88px;top:95px;width:382px;height:35px;font-family:"Libre Baskerville",serif;font-size:15px;font-weight:700;letter-spacing:.3px}
.truck{left:775px;top:1721px;width:359px;height:247px;border-radius:14px;background:linear-gradient(180deg,#f5b73a 0%,#f7d58a 50%,#e4e4e4 100%)}

/* products */
.kicker{left:0;top:2033px;width:1200px;text-align:center;font-size:17px;letter-spacing:.5px;color:#4f4a44}
.tabs .tab{top:2134px;height:35px;border:1.5px solid var(--gold);border-radius:18px;color:var(--gold-dark);font-size:14px;display:flex;align-items:center;justify-content:center}
.tabs .tab.on{background:var(--gold);color:var(--white)}
.product{top:2203px;width:262px;text-align:center}
.product .photo{margin:0 auto;width:200px;height:205px;border-radius:10px}
.product.active .photo{width:225px;height:225px;background:#f2d08e}
.product .stars{margin-top:22px;color:var(--gold);font-size:13px;letter-spacing:2px}
.product h4{font-size:17px;font-weight:500;color:var(--ink);margin-top:2px;white-space:nowrap}
.product .price{font-size:18px;font-weight:600;color:var(--gold-dark);margin-top:6px}
.new-tag{left:10px;top:14px;background:#f5b73a;color:var(--white);font-size:11px;padding:1px 8px}
.quick{top:110px;width:36px;height:36px;border-radius:50%;display:flex;align-items:center;justify-content:center;background:var(--white)}

/* locations */
.locations{left:0;top:2577px;width:1200px;height:278px;background:var(--cream)}
.locations h2{left:0;top:22px;width:1200px;text-align:center;font-size:40px}
.loc{top:99px;width:320px;text-align:center}
.loc svg{display:block;margin:0 auto}
.loc p{margin-top:24px;font-size:17px;line-height:25px;font-weight:500;color:#7a7167}

/* newsletter */
.newsletter{left:0;top:2936px;width:1200px;height:216px;background:var(--cream)}
.newsletter h2{left:0;top:12px;width:1200px;text-align:center;font-size:44px}
.newsletter p{left:360px;top:68px;width:480px;text-align:center;font-family:"Libre Baskerville",serif;font-size:13px;line-height:21px;color:#6b655d}
.newsletter .field{left:402px;top:132px;width:270px;height:49px;border:1px solid #d9d4c6;background:var(--white);font-family:"Libre Baskerville",serif;font-size:13px;color:#6b655d;padding:15px 14px}
.newsletter .send{left:687px;top:132px;width:114px;height:49px;background:var(--gold);color:var(--white);font-size:14px;font-weight:500;display:flex;align-items:center;justify-content:center}
.spark{color:#e8e0c6;font-size:22px}

/* footer */
.footer{left:0;top:3152px;width:1200px;height:305px;background:var(--gold)}
.footer-brand{left:65px;top:80px;width:270px;height:110px;background:#f9e7b5;border-radius:8px;display:flex;align-items:center;justify-content:center;gap:10px;font-size:28px;font-weight:600;color:var(--red)}
.footer-brand .dot{width:14px;height:14px;border-radius:50%;background:var(--red)}
.social{top:220px;width:50px;height:48px;background:var(--white);border-radius:3px}
.footer h3{top:36px;font-family:"Libre Baskerville",serif;font-weight:700;font-size:22px;color:var(--white)}
.seal{top:102px;width:62px;height:62px;border-radius:50%;background:#2e4a6e;border:4px solid #cfd6de}
.cert{left:376px;top:176px;width:137px;height:88px;background:var(--white);border:5px solid #1d9bc4;border-radius:3px}
.links{left:593px;top:102px;list-style:none;font-family:"Libre Baskerville",serif;font-weight:700;font-size:17px;line-height:33.5px;color:var(--white)}
.links li::before{content:"•";margin-right:9px}
.contact{left:819px;top:102px;font-family:"Libre Baskerville",serif;font-weight:700;font-size:16px;line-height:25px;color:var(--white)}
.copyright{left:0;top:3457px;width:1200px;height:30px;text-align:center;font-family:"Libre Baskerville",serif;font-size:14px;line-height:30px;color:#6b655d}
</style>
</head>
<body>

<header class="abs site-header">
  <div class="abs brand"><span class="dot"></span>Bäckerei Lindner</div>
  <svg class="abs search" width="22" height="22" viewBox="0 0 22 22" fill="none" stroke="#3d3a36" stroke-width="2"><circle cx="9" cy="9" r="7"/><path d="M14 14l6 6"/></svg>
  <nav class="abs nav">
    <span>Home</span><span>Aktuelles &amp; Aktionen</span><span>Onlineshop</span><span>Filialen</span><span>Mobile Bäckerei</span><span>Backwaren</span><span>Torten</span><span>Engagement</span><span>Historie</span><span>Kontakt</span>
  </nav>
  <div class="abs user-icons"><span></span><span></span></div>
  <div class="abs cart">My Cart<b>0 item</b></div>
</header>

<section class="abs hero">
  <div class="abs hero-photo" role="img" aria-label="Backzutaten: Eier, Zimtstangen, Mehl und Schneebesen auf hellem Tisch"></div>
  <h1 class="abs script">Herzlich Willkommen bei der<br>Bäckerei Lindner!</h1>
  <p class="abs">Wir sind eine Bäckerei in der 4. Generation im Herzen des Erzgebirges.<br>Wir backen mit Liebe und hochwertigen Rohstoffen.<br>... Und wir verwenden "Belebtes Wasser" für unsere Produkte</p>
  <div class="abs btn">JETZT EINKAUFEN</div>
</section>

<section class="abs features">
  <div class="abs feature" style="left:107px"><div class="ico" role="img" aria-label="Lieferwagen"></div><div><h3>Free Shipping</h3><p>On orders over $29</p></div></div>
  <div class="abs feature" style="left:371px"><div class="ico" style="width:56px" role="img" aria-label="Geschenkbox"></div><div><h3>Free Gift Box</h3><p>Full cake eating utensils</p></div></div>
  <div class="abs feature" style="left:597px"><div class="ico" role="img" aria-label="Heiße Speise in Topfhandschuhen"></div><div><h3>Order Upon Request</h3><p>Follow the model you sent</p></div></div>
  <div class="abs feature" style="left:879px"><div class="ico" style="width:60px" role="img" aria-label="Kuchen"></div><div><h3>Refund For Product</h3><p>The cake is not the same</p></div></div>
</section>

<h2 class="abs sec-title script" style="top:768px"><i></i>Aktuelles &amp; Aktionen<i></i></h2>

<article class="abs news" style="left:65px">
  <div class="abs photo" role="img" aria-label="Geburtstagstorte mit goldenem Schriftzug" style="background:linear-gradient(160deg,#f3f1ee,#e9d9b8 60%,#f4c35a)"></div>
  <div class="abs off">50%<br>Off</div>
  <h3 class="abs script">50 % Rabatt für heute</h3>
  <p class="abs">Lorem Ipsum is simply dummy text of the printing and typesetting industry. Lorem Ipsum has been the industry's standard dummy text ever since the 1500s</p>
</article>
<article class="abs news" style="left:612px">
  <div class="abs photo" role="img" aria-label="Cupcakes mit Sahnehaube" style="background:linear-gradient(160deg,#efe6dc,#e8d2b4 50%,#8c5a3a)"></div>
  <div class="abs off">30%<br>Off</div>
  <h3 class="abs script">Ihre Kundenkarte</h3>
  <p class="abs">Lorem Ipsum is simply dummy text of the printing and typesetting industry. Lorem Ipsum has been the industry's standard dummy text ever since the 1500s</p>
</article>
<div class="abs dots"><span></span><span></span><span class="on"></span><span></span></div>

<h2 class="abs sec-title script" style="top:1158px"><i></i>Backwaren<i style="background:var(--red);margin-left:90px"></i></h2>

<div class="abs cat" style="left:66px;top:1216px"><div class="abs photo" role="img" aria-label="Erdbeer-Sahnetorte" style="background:linear-gradient(150deg,#f4f2ef,#f3d9d2 50%,#e9e2d6)"></div><div class="abs label script">Fruchtiges</div></div>
<div class="abs cat" style="left:424px;top:1216px"><div class="abs photo" role="img" aria-label="Gemüsequiche" style="background:linear-gradient(150deg,#3a3a36,#c9b27a 50%,#8a8c5a)"></div><div class="abs label script">Cremiges</div></div>
<div class="abs cat" style="left:786px;top:1216px"><div class="abs photo" role="img" aria-label="Karottenkuchen" style="background:linear-gradient(150deg,#e9e5e0,#b8744a 55%,#e8c4c4)"></div><div class="abs label script">Sahniges</div></div>
<div class="abs cat" style="left:66px;top:1473px"><div class="abs photo" role="img" aria-label="Gugelhupf mit Zuckerguss" style="background:linear-gradient(150deg,#eeece6,#d9a55a 55%,#ecebe4)"></div><div class="abs label script">Besonderes</div></div>
<div class="abs cat" style="left:424px;top:1473px"><div class="abs photo" role="img" aria-label="Jubiläumstorte mit goldener Deko" style="background:linear-gradient(150deg,#ffffff,#e6d6b6 55%,#c8a25a)"></div><div class="abs label script">Vielfalt</div></div>
<div class="abs cat" style="left:786px;top:1473px"><div class="abs photo" role="img" aria-label="Hochzeitstorte mit Brautpaar-Aufsatz" style="background:linear-gradient(150deg,#c98a2a,#f3d27a 50%,#f6f0e0)"></div><div class="abs label script">Hochzeit</div></div>

<section class="abs mobile">
  <h2 class="abs script">Ihr Bäcker-Auto kommt zu Ihnen...</h2>
  <div class="abs btn">MOBILEN VERKAUFSPLAN ANZEIGEN</div>
</section>
<div class="abs truck" role="img" aria-label="Gelber Verkaufswagen der mobilen Bäckerei"></div>

<p class="abs kicker">BESTER GESCHMACK VON DESSERTS</p>
<h2 class="abs sec-title script" style="top:2064px;font-size:30px">Unsere Produkte</h2>
<div class="tabs">
  <div class="abs tab on" style="left:436px;width:100px">Fruchtiges</div>
  <div class="abs tab" style="left:553px;width:117px">Cremiges</div>
  <div class="abs tab" style="left:687px;width:94px">Sahniges</div>
</div>

<div class="abs product" style="left:-57px"><div class="photo" role="img" aria-label="Schichttorte mit Keksen und Kirschen" style="background:linear-gradient(180deg,#2b2724,#f2e6c4 55%,#fff)"></div><div class="stars">★★★★★</div><h4>Four-Layer Fruit Cake</h4><div class="price">Euro15.00</div></div>
<div class="abs product" style="left:204px"><div class="photo" role="img" aria-label="Geburtstagstorte mit Früchten" style="background:linear-gradient(180deg,#fff,#f6d86a 45%,#f3efe2)"></div><div class="stars">★★★★★</div><h4>Chocolate Covered Cake</h4><div class="price">Euro15.00</div></div>
<div class="abs product active" style="left:467px">
  <div class="photo" role="img" aria-label="Jubiläumstorte mit goldenen Zahlen" style="position:relative">
    <span class="abs new-tag">New</span>
    <span class="abs quick" style="left:36px;background:var(--gold)"><svg width="16" height="16" viewBox="0 0 16 16" fill="none" stroke="#fff" stroke-width="1.6"><path d="M1 2h2l2 8h8l2-6H4"/><circle cx="6" cy="13" r="1"/><circle cx="12" cy="13" r="1"/></svg></span>
    <span class="abs quick" style="left:94px"><svg width="16" height="16" viewBox="0 0 16 16" fill="none" stroke="#3d3a36" stroke-width="1.5"><path d="M8 14S2 10 2 6a3 3 0 016-1 3 3 0 016 1c0 4-6 8-6 8z"/></svg></span>
    <span class="abs quick" style="left:152px"><svg width="18" height="14" viewBox="0 0 18 14" fill="none" stroke="#3d3a36" stroke-width="1.5"><path d="M1 7s3-5 8-5 8 5 8 5-3 5-8 5-8-5-8-5z"/><circle cx="9" cy="7" r="2"/></svg></span>
  </div>
  <div class="stars" style="margin-top:18px">★★★★★</div><h4>Four-Layer Fruit Cake</h4><div class="price">Euro15.00</div></div>
<div class="abs product" style="left:729px"><div class="photo" role="img" aria-label="Geburtstagstorte mit goldenem Aufsatz" style="background:linear-gradient(180deg,#fff,#e8c370 50%,#f5efe6)"></div><div class="stars">★★★★★</div><h4>Chocolate Covered Cake</h4><div class="price">Euro15.00</div></div>
<div class="abs product" style="left:991px"><div class="photo" role="img" aria-label="Weiße Torte mit roten Blüten" style="background:linear-gradient(180deg,#b8262b,#efe9de 45%,#fff)"></div><div class="stars">★★★★★</div><h4>Chocolate Covered Cake</h4><div class="price">Euro15.00</div></div>

<section class="abs locations">
  <h2 class="abs script">drei Standorte: Hauptsitz</h2>
  <div class="abs loc" style="left:65px">
    <svg width="84" height="84" viewBox="0 0 84 84"><circle cx="42" cy="42" r="40" fill="#e7ae4c"/><path d="M42 24a11 11 0 00-11 11c0 9 11 22 11 22s11-13 11-22a11 11 0 00-11-11z" fill="#fff"/><circle cx="42" cy="35" r="4" fill="#e7ae4c"/></svg>
    <p>Lindenweg 14, 09619 -<br>Talheim - Bergstraße<br>8, 09599 Eichau</p>
  </div>
  <div class="abs loc" style="left:441px">
    <svg width="84" height="84" viewBox="0 0 84 84"><circle cx="42" cy="42" r="40" fill="#e7ae4c"/><path d="M42 24a11 11 0 00-11 11c0 9 11 22 11 22s11-13 11-22a11 11 0 00-11-11z" fill="#fff"/><circle cx="42" cy="35" r="4" fill="#e7ae4c"/></svg>
    <p>Marktgasse 5, 09599 Eichau</p>
  </div>
  <div class="abs loc" style="left:826px">
    <svg width="84" height="84" viewBox="0 0 84 84"><circle cx="42" cy="42" r="40" fill="#e7ae4c"/><path d="M42 24a11 11 0 00-11 11c0 9 11 22 11 22s11-13 11-22a11 11 0 00-11-11z" fill="#fff"/><circle cx="42" cy="35" r="4" fill="#e7ae4c"/></svg>
    <p>Mühlenring 3, 09623,<br>Waldhausen-Mühle</p>
  </div>
</section>

<section class="abs newsletter">
  <span class="abs spark" style="left:34px;top:50px">✦</span>
  <span class="abs spark" style="left:60px;top:95px">+</span>
  <span class="abs spark" style="left:4px;top:125px">✦</span>
  <span class="abs spark" style="left:1175px;top:125px;font-size:14px">✦</span>
  <h2 class="abs script">Abonniere den Newsletter Newsletter</h2>
  <p class="abs">Melden Sie sich für unseren Newsletter an und erhalten Sie den Rabattcode.</p>
  <div class="abs field">Ihre E-Mail-Adresse</div>
  <div class="abs send">SENDEN</div>
</section>

<footer class="abs footer">
  <div class="abs footer-brand"><span class="dot"></span>Bäckerei Lindner</div>
  <div class="abs social" style="left:152px"></div>
  <div class="abs social" style="left:212px"></div>
  <h3 class="abs" style="left:387px">Sicherheit</h3>
  <div class="abs seal" style="left:376px"></div>
  <div class="abs seal" style="left:448px;background:#3c5f86"></div>
  <div class="abs cert"></div>
  <h3 class="abs" style="left:593px">Link</h3>
  <ul class="abs links">
    <li>Aktuelles &amp; Aktionen</li><li>Onlineshop</li><li>Filialen</li><li>Historie</li><li>Engagement</li><li>Torten</li>
  </ul>
  <h3 class="abs" style="left:819px">Kontakt</h3>
  <div class="abs contact">Tel. 037111 4820 |<br>E-Mail: info@baeckerei-lindner.de</div>
</footer>
<div class="abs copyright">Copyright 2024, baeckerei-lindner.de</div>

</body>
</html>
```